Concrete Construction Business Card design

We are a commercial concrete construction company based in Texas. a family owned business which our trade was passed down and taught by our grandfather whom we want represented in this design. our grandfathers nick name was "pepe" so we are wanting the letter G to be symbolized in some way with a red pepe . colors should be possibly a grey color back ground , green letter g and red pepe pepper , to be left for you to decide with integrity , concrete professionalism,and mexican heritage

Target Market(s)

general contractors, architects,inverstors, and engineers

Industry/Entity Type

Concrete

Contact Information for Business Card

Herrera Concrete Construction LLC, Dennis Herrera, 1872 Bramblewood Ln. Denton, TX 76209, (940)318-2746, dhslabworkllc48@quarrymail.net

```html
<!DOCTYPE html>
<html lang="en">
<head>
<meta charset="utf-8">
<title>Herrera Concrete Construction – Business Card</title>
<link rel="stylesheet" href="https://fonts.googleapis.com/css2?family=Roboto:wght@400;700&family=Roboto+Condensed:ital,wght@1,400&display=swap">
<style>
  :root {
    --card-bg: #e6e7e9;
    --ink: #333333;
    --brand-green: #a4cf4a;
    --name-blue: #1a9ad6;
    --pin-blue: #2a9fd8;
    --phone-orange: #f47b20;
    --mail-grey: #6d6e71;
    --mail-flap: #b9e02b;
  }
  html, body {
    margin: 0;
    padding: 0;
    overflow: hidden;
    background: var(--card-bg);
  }
  .card {
    position: relative;
    width: 1200px;
    height: 704px;
    background: var(--card-bg);
    font-family: "Roboto", Arial, sans-serif;
    color: var(--ink);
    overflow: hidden;
  }
  .brand {
    position: absolute;
    left: 0;
    right: 0;
    top: 150px;
    text-align: center;
    color: var(--ink);
    font-weight: 700;
  }
  .brand-mark {
    display: inline-flex;
    align-items: center;
    gap: 18px;
  }
  .brand-dot {
    width: 40px;
    height: 40px;
    border-radius: 50%;
    background: var(--brand-green);
  }
  .brand-name {
    font-size: 62px;
    letter-spacing: 2px;
    line-height: 1;
  }
  .brand-trade {
    display: block;
    margin-top: 14px;
    font-size: 53px;
    line-height: 1;
  }
  .person {
    position: absolute;
    left: 225px;
    top: 375px;
    margin: 0;
    font-family: "Roboto Condensed", "Arial Narrow", sans-serif;
    font-style: italic;
    font-weight: 400;
    font-size: 50px;
    color: var(--name-blue);
  }
  .contact {
    position: absolute;
    left: 0;
    top: 0;
    margin: 0;
    padding: 0;
    list-style: none;
    font-size: 25px;
    line-height: 33px;
  }
  .contact-item {
    position: absolute;
    left: 0;
    white-space: nowrap;
  }
  .contact-icon {
    position: absolute;
  }
  .contact-text {
    position: absolute;
    left: 225px;
  }
  .contact-address { top: 478px; }
  .contact-address .contact-icon { left: 141px; top: 0; }
  .contact-phone { top: 560px; }
  .contact-phone .contact-icon { left: 144px; top: 0; }
  .contact-email { top: 603px; }
  .contact-email .contact-icon { left: 130px; top: 2px; }
</style>
</head>
<body>
<main class="card">
  <header class="brand">
    <div class="brand-mark">
      <span class="brand-dot"></span>
      <span class="brand-name">HERRERA</span>
    </div>
    <span class="brand-trade">Concrete Construction</span>
  </header>

  <h1 class="person">Dennis Herrera</h1>

  <ul class="contact">
    <li class="contact-item contact-address">
      <svg class="contact-icon" width="26" height="38" viewBox="0 0 26 38" aria-hidden="true">
        <path d="M13 2 C6.5 2 2 6.8 2 12.8 C2 21 13 35 13 35 C13 35 24 21 24 12.8 C24 6.8 19.5 2 13 2 Z" fill="none" stroke="var(--pin-blue)" stroke-width="3.5"/>
        <circle cx="13" cy="12.5" r="4" fill="var(--mail-flap)"/>
      </svg>
      <span class="contact-text">1872 Bramblewood Ln. Denton<br>TX 76209</span>
    </li>
    <li class="contact-item contact-phone">
      <svg class="contact-icon" width="20" height="34" viewBox="0 0 20 34" aria-hidden="true">
        <rect x="1" y="1" width="18" height="32" rx="3" fill="var(--phone-orange)"/>
        <rect x="4" y="4" width="12" height="9" fill="#fde3cf"/>
        <g fill="#fde3cf">
          <rect x="4" y="16" width="3" height="3"/><rect x="8.5" y="16" width="3" height="3"/><rect x="13" y="16" width="3" height="3"/>
          <rect x="4" y="21" width="3" height="3"/><rect x="8.5" y="21" width="3" height="3"/><rect x="13" y="21" width="3" height="3"/>
          <rect x="4" y="26" width="3" height="3"/><rect x="8.5" y="26" width="3" height="3"/><rect x="13" y="26" width="3" height="3"/>
        </g>
      </svg>
      <span class="contact-text">(940)318-2746</span>
    </li>
    <li class="contact-item contact-email">
      <svg class="contact-icon" width="48" height="32" viewBox="0 0 48 32" aria-hidden="true">
        <rect x="0" y="2" width="48" height="30" fill="var(--mail-grey)"/>
        <path d="M0 2 L24 18 L48 2 Z" fill="var(--mail-flap)"/>
        <path d="M0 32 L19 16 M48 32 L29 16" stroke="#5a5b5e" stroke-width="1.5"/>
      </svg>
      <span class="contact-text">dhslabworkllc48@quarrymail.net</span>
    </li>
  </ul>
</main>
</body>
</html>
```